Boutique Financial Services firm require Custom Christmas Card

We are Brindle Court, a Melbourne based financial services firm that offer high quality financial solutions to our clients. We need a Christmas Card to send to our valued clients that evokes our exceptional quality, care and thoughtfulness of our bespoke financial advice.
The design must be elegant and simple, incorporating our "tree" logo and brand colour. Please have a look at our website to further understand our brand: https://brindlevq.example/. I've attached the Christmas card which was created last year for reference.
The interior of the card must include a simple message such as "Season's Greetings" or "Merry Christmas" and the back of the card must list "Contact Details: 12/71 Wexford Lane, Melbourne VIC 3000, 03 7415 3862, hello@brindlevq.example"
The new Christmas card must be formatted as per below print format:
- Spread size: 250mm x 194mm
- Finished size: 125mm x 194mm
The design must also be provided in digital formats (Facebook, Instagram) for social media posting.
Please submit a minimum of 2 design options per designer. We must confirm our card design by Thurs Dec 6 to allow time for printing & posting.
Target Market(s)
Men & women, aged 35-70, with families, own their own home, wealthy, enjoys the finer things in life. Please have a look at our website to further understand our brand: https://brindlevq.example/.
Industry/Entity Type
Financial Service
Colors
Designer to choose colors to be used in the design.
Requirements
Must have
- The design must be elegant, simple and evoke Christmas spirits. We would like our logo and brand colour incorporated somehow. I've attached our brand guidelines and the Christmas card which was created last year for your reference.
- The front & interior of the card must include a simple message such as "Season's Greetings" or "Merry Christmas" and the back of the card must list "Contact Details: Brindle Court, 12/71 Wexford Lane, Melbourne VIC 3000, 03 7415 3862, hello@brindlevq.example"
- The new Christmas card must be formatted as per below print format:
- - Spread size: 250mm x 194mm
- - Finished size: 125mm x 194mm
- The design must also be provided in digital formats (Facebook, Instagram) for social media posting.

```html
<!DOCTYPE html>
<html lang="en">
<head>
<meta charset="utf-8">
<title>Brindle Court Holiday Card</title>
<link rel="stylesheet" href="https://fonts.googleapis.com/css2?family=Cabin:wght@400;600&family=Pinyon+Script&family=Sacramento&display=swap">
<style>
  :root {
    --page: #eceeea;
    --olive-deep: #8e9a1b;
    --olive: #a9b61f;
    --olive-light: #b7c228;
    --paper: #ffffff;
    --ink: #1c1c1c;
    --ink-soft: #333333;
  }
  * { box-sizing: border-box; margin: 0; padding: 0; }
  html, body {
    width: 721px; height: 1200px; overflow: hidden;
    background: var(--page);
    font-family: "Cabin", "Gill Sans", sans-serif;
  }
  .spread {
    position: absolute; left: 20px; width: 681px; height: 528px;
    box-shadow: 0 3px 10px rgba(0,0,0,0.18);
    overflow: hidden;
  }
  .spread--outer {
    top: 40px;
    background: linear-gradient(180deg, var(--olive-deep) 0%, var(--olive) 55%, var(--olive-light) 80%);
  }
  .spread--inner { top: 620px; background: var(--paper); }

  .fold {
    position: absolute; top: 0; bottom: 0; left: 340px; width: 1px;
    background: rgba(0,0,0,0.05);
  }

  .snow-border--bottom {
    position: absolute; left: 0; right: 0; top: 396px; height: 94px;
    background: linear-gradient(180deg, rgba(255,255,255,0) 0%, rgba(255,255,255,0.35) 40%, rgba(255,255,255,0.8) 75%, var(--paper) 100%);
  }
  .snow-ground {
    position: absolute; left: 0; right: 0; top: 490px; bottom: 0;
    background: var(--paper);
  }

  .contact {
    position: absolute; left: 136px; top: 412px; width: 120px;
    text-align: center; color: var(--ink);
    font-size: 8.5px; line-height: 11px; font-weight: 600;
  }

  .greeting {
    position: absolute; left: 372px; width: 300px;
    text-align: center;
    font-family: "Sacramento", cursive; font-weight: 400;
    line-height: 1;
    white-space: nowrap;
  }
  .greeting__word { display: block; }
  .greeting--front { top: 150px; color: var(--paper); }
  .greeting--inner { top: 170px; color: var(--olive); }
  .greeting__word--first { font-size: 62px; margin-left: 14px; }
  .greeting__word--second { font-size: 68px; margin-top: 2px; }

  .inner-band {
    position: absolute; left: 0; right: 0; top: 0; height: 32px;
    background: linear-gradient(90deg, var(--olive-deep), var(--olive-light) 50%, var(--olive-deep));
  }
  .snow-border--top {
    position: absolute; left: 0; right: 0; top: 32px; height: 76px;
    background: linear-gradient(180deg, var(--olive) 0%, rgba(169,182,31,0.5) 40%, rgba(169,182,31,0.15) 75%, rgba(169,182,31,0) 100%);
  }

  .lead-in {
    position: absolute; left: 430px; top: 134px; width: 160px;
    text-align: center; font-size: 10.5px; color: var(--ink-soft);
  }

  .sign-off {
    position: absolute; right: 28px; top: 436px; text-align: right;
  }
  .sign-off__signature {
    font-family: "Pinyon Script", cursive; font-size: 21px; color: var(--ink);
    line-height: 26px;
  }
  .sign-off__name {
    font-size: 8.5px; font-weight: 600; color: var(--ink-soft); margin-top: 2px;
  }
  .brand {
    display: flex; align-items: center; justify-content: flex-end; gap: 4px;
    margin-top: 7px;
  }
  .brand__dot {
    width: 16px; height: 16px; border-radius: 50%; background: var(--olive);
  }
  .brand__name {
    font-size: 12px; font-weight: 600; color: var(--ink-soft);
  }
</style>
</head>
<body>
  <section class="spread spread--outer" aria-label="Card outside: back and front">
    <div class="fold"></div>
    <div class="snow-border--bottom" role="img" aria-label="Border of white snowflakes and snow dots rising from the bottom edge"></div>
    <div class="snow-ground"></div>
    <div class="contact">
      12/71 Wexford Lane<br>
      Melbourne VIC 3000<br>
      03 7415 3862<br>
      hello@brindlevq.example
    </div>
    <h1 class="greeting greeting--front">
      <span class="greeting__word greeting__word--first">Happy</span>
      <span class="greeting__word greeting__word--second">Holidays</span>
    </h1>
  </section>

  <section class="spread spread--inner" aria-label="Card inside">
    <div class="inner-band"></div>
    <div class="snow-border--top" role="img" aria-label="Border of olive snowflakes and dots hanging from the top band"></div>
    <p class="lead-in">Wishing you a very</p>
    <h2 class="greeting greeting--inner">
      <span class="greeting__word greeting__word--first">Happy</span>
      <span class="greeting__word greeting__word--second">Holidays</span>
    </h2>
    <div class="sign-off">
      <p class="sign-off__signature">Rowan Ashby</p>
      <p class="sign-off__name">Rowan Ashby CEO &amp; Brindle Team</p>
      <div class="brand">
        <span class="brand__dot"></span>
        <span class="brand__name">Brindle Court</span>
      </div>
    </div>
  </section>
</body>
</html>
```